New Business Card Design for Manufacturing

We are an engineering/manufacturing company that offers Advanced machining/assembly/engineering services, as well as innovative products for the heavy duty engine cooling markets.

We are looking to get a new business card designed that is clean and modern looking, but still fits the wide range of technical/skilled work we do.

- We hope to use this design as the base for other design work in new Presentations, web, and print work.

Industry/Entity Type

Engineering

Contact Information for Business Card

Our preferred color of blue is (RGB) 22/71/159 but can vary slightly from that color. Our content will be our Logo and full company name (Fabricated Tooling Works, Inc.), company address, name, job title, phone number with extension, cell number, fax number, website, and email address on the cards.
We'd like the full company name next to the logo, but we are open to other interpretations of that layout.
Preferably, we would like the back side to be clean with just our logo, and the front to contain all of the contact information.

Colors
2f74b4
0355a3
85abd2

Requirements
Must have
• - Logo, company name, needed content - We are open to interpretation beyond that.
• - Standard size business card.
• - Horizontal orientation.
• - Enough space for lengthy names / job titles (for example, a job title could read "Directory of Human Resources" or "V.P. of Governmental Affairs"). We need this to look clean, whether the title be short (CEO) or long (as described above).

```html
<!DOCTYPE html>
<html lang="en">
<head>
<meta charset="utf-8">
<title>Fabricated Tooling Works – Business Card</title>
<link href="https://fonts.googleapis.com/css2?family=Lato:wght@300;400;700;900&display=swap" rel="stylesheet">
<style>
  :root {
    --brand-blue: #1667bf;
    --brand-deep: #0355a3;
    --brand-navy: #16479f;
    --brand-mid: #2f74b4;
    --brand-light: #85abd2;
    --paper: #f4f5f6;
    --white: #ffffff;
    --stage: #e9ebee;
  }
  * { box-sizing: border-box; margin: 0; padding: 0; }
  html, body { width: 1200px; height: 780px; overflow: hidden; }
  body {
    background: var(--stage);
    font-family: "Lato", Arial, sans-serif;
    display: flex;
    align-items: center;
    justify-content: center;
    gap: 40px;
  }
  .card {
    position: relative;
    width: 540px;
    height: 309px;
    overflow: hidden;
    background: linear-gradient(160deg, var(--brand-blue) 0%, var(--brand-deep) 100%);
    color: var(--white);
    box-shadow: 0 6px 18px rgba(0, 0, 0, 0.18);
  }
  .card-front .wave { position: absolute; inset: 0; width: 100%; height: 100%; }
  .brand-name {
    font-weight: 900;
    letter-spacing: 1px;
    line-height: 1;
  }
  .card-front .brand {
    position: absolute;
    top: 30px;
    left: 150px;
    color: var(--brand-navy);
  }
  .card-front .brand-name { font-size: 62px; }
  .tagline {
    font-weight: 700;
    font-size: 12px;
    letter-spacing: 1px;
    text-transform: uppercase;
    margin-top: 6px;
  }
  .holder {
    position: absolute;
    left: 30px;
    top: 196px;
  }
  .holder-name { font-weight: 700; font-size: 16px; text-transform: uppercase; letter-spacing: .5px; }
  .holder-title { font-weight: 300; font-size: 13px; margin-top: 2px; }
  .contact {
    position: absolute;
    left: 260px;
    top: 178px;
    font-size: 11.5px;
    font-weight: 400;
    line-height: 1.45;
  }
  .address { margin-bottom: 8px; }
  .contact-list { list-style: none; }
  .contact-list li { display: flex; align-items: center; gap: 8px; height: 18px; }
  .contact-list svg { width: 13px; height: 13px; flex: none; }

  .card-back .brand {
    position: absolute;
    left: 70px;
    top: 92px;
    color: var(--white);
  }
  .card-back .brand-name { font-size: 84px; }
  .card-back .tagline { font-size: 14px; margin-top: 8px; }
  .company-name {
    position: absolute;
    left: 300px;
    top: 110px;
    font-weight: 900;
    font-size: 17px;
    line-height: 1.05;
    text-transform: uppercase;
  }
  .company-name small { font-size: 9px; }
  .website {
    position: absolute;
    left: 0; right: 0;
    bottom: 46px;
    text-align: center;
    font-weight: 300;
    font-size: 13px;
    letter-spacing: 5px;
  }
</style>
</head>
<body>

  <section class="card card-front" aria-label="Card front">
    <svg class="wave" viewBox="0 0 540 309" preserveAspectRatio="none" aria-hidden="true">
      <path d="M0,0 H540 V8 C470,150 260,182 0,170 Z" fill="var(--brand-light)" opacity="0.85"/>
      <path d="M0,0 H540 V0 C460,130 250,160 0,152 Z" fill="var(--paper)"/>
    </svg>
    <div class="brand">
      <div class="brand-name">FTW</div>
      <div class="tagline">Built to Tolerance</div>
    </div>
    <div class="holder">
      <div class="holder-name">Daniel Harper</div>
      <div class="holder-title">Founder</div>
    </div>
    <div class="contact">
      <div class="address">PO Box 418 Foundry Lane<br>27 Harbour Road Geelong</div>
      <ul class="contact-list">
        <li>
          <svg viewBox="0 0 14 14"><circle cx="7" cy="7" r="6.5" fill="none" stroke="#fff"/><rect x="5" y="3.5" width="4" height="7" rx="1" fill="#fff"/></svg>
          (555) 310-2284
        </li>
        <li>
          <svg viewBox="0 0 14 14"><circle cx="7" cy="7" r="6.5" fill="none" stroke="#fff"/><path d="M4 5.5 Q7 3 10 5.5 L9 7 L8 6.3 H6 L5 7 Z M4.5 8 H9.5 V10 H4.5 Z" fill="#fff"/></svg>
          (555) 310-2291
        </li>
        <li>
          <svg viewBox="0 0 14 14"><circle cx="7" cy="7" r="6.5" fill="none" stroke="#fff"/><rect x="3.8" y="4.8" width="6.4" height="4.6" fill="#fff"/><path d="M3.8 4.8 L7 7.4 L10.2 4.8" fill="none" stroke="var(--brand-blue)" stroke-width=".8"/></svg>
          info@fabtoolworks.com
        </li>
        <li>
          <svg viewBox="0 0 14 14"><circle cx="7" cy="7" r="6.5" fill="none" stroke="#fff"/><circle cx="7" cy="7" r="3.5" fill="none" stroke="#fff" stroke-width=".9"/><path d="M3.5 7 H10.5 M7 3.5 V10.5" stroke="#fff" stroke-width=".8"/></svg>
          www.fabtoolworks.com
        </li>
      </ul>
    </div>
  </section>

  <section class="card card-back" aria-label="Card back">
    <div class="brand">
      <div class="brand-name">FTW</div>
      <div class="tagline">Built to Tolerance</div>
    </div>
    <div class="company-name">Fabricated<br>Tooling<br>Works <small>Inc</small></div>
    <div class="website">www.fabtoolworks.com</div>
  </section>

</body>
</html>
```